Dentist Anesthesiologist
BrookMint Dental
Professional
Rafael Okonkwo, DMD, MPH, MBA
418 North Pine Hollow Road
Suite 207915
Phoenix, Arizona 85093
(877) 555-TOOL (8665)
(480) 555-TOOL (8665)
Dr.Okonkwo@BrookMintDental.example
www.BrookMintDental.example
Please visit my website www.BrookMintDental.example for colors (blue and brown). I am not sure if I want my name to be written as Dr. Rafael Okonkwo or Rafael Okonkwo, DMD, MPH, MBA. In the form above, it didn't ask for the business name - it is BrookMint Dental.
I am okay with textual information or the logo design on the back of the card.
Here is the logo design on my website.
Here is the logo design for my website.

```html
<!DOCTYPE html>
<html lang="en">
<head>
<meta charset="utf-8">
<title>BrookMint – Business Card</title>
<link rel="stylesheet" href="https://fonts.googleapis.com/css2?family=Open+Sans:wght@400;600&display=swap">
<style>
  :root {
    --canvas-bg: #ecebe8;
    --brand-blue: #3b86c8;
    --brand-blue-light: #5ea3dd;
    --brand-blue-dark: #2a6eaf;
    --brand-brown: #a87c4f;
    --gold-rule: #c9a46e;
    --card-white: #ffffff;
    --text-white: #ffffff;
    --card-shadow: rgba(0, 0, 0, 0.18);
  }
  * { box-sizing: border-box; margin: 0; padding: 0; }
  html, body { width: 1200px; height: 629px; overflow: hidden; }
  body {
    background: var(--canvas-bg);
    font-family: "Open Sans", Arial, sans-serif;
    position: relative;
  }
  .card {
    position: absolute;
    top: 166px;
    width: 520px;
    height: 297px;
    border-radius: 4px;
    overflow: hidden;
    box-shadow: 0 6px 18px var(--card-shadow);
  }
  .brand-lockup { display: flex; align-items: center; gap: 12px; }
  .brand-dot { width: 14px; height: 14px; border-radius: 50%; flex: none; }
  .brand-name {
    font-family: "Open Sans", Arial, sans-serif;
    font-weight: 400;
    letter-spacing: 0.5px;
    line-height: 1;
  }
  .tagline {
    font-family: "Open Sans", Arial, sans-serif;
    text-transform: uppercase;
    letter-spacing: 3px;
  }

  /* Back of card */
  .card-back {
    left: 50px;
    background: linear-gradient(135deg, var(--brand-blue-light) 0%, var(--brand-blue) 55%, var(--brand-blue-dark) 100%);
    display: flex;
    flex-direction: column;
    align-items: center;
    justify-content: center;
    color: var(--text-white);
  }
  .card-back .brand-name { font-size: 40px; color: var(--text-white); }
  .card-back .brand-dot { background: var(--text-white); }
  .card-back .tagline { font-size: 12px; margin-top: 14px; color: var(--text-white); }

  /* Front of card */
  .card-front { left: 630px; background: var(--card-white); }
  .front-header {
    height: 150px;
    display: flex;
    flex-direction: column;
    align-items: center;
    justify-content: center;
  }
  .front-header .brand-name { font-size: 38px; color: var(--brand-blue); }
  .front-header .brand-dot { background: var(--brand-blue); }
  .front-header .tagline { font-size: 11.5px; margin-top: 14px; color: var(--brand-brown); }
  .gold-rule { height: 3px; background: var(--gold-rule); }
  .front-footer {
    height: 144px;
    background: linear-gradient(135deg, var(--brand-blue-light) 0%, var(--brand-blue) 60%, var(--brand-blue-dark) 100%);
    color: var(--text-white);
    display: flex;
    justify-content: space-between;
    padding: 20px 22px 18px;
    font-size: 10px;
    line-height: 1.55;
  }
  .practitioner { display: flex; flex-direction: column; justify-content: space-between; }
  .practitioner-name { font-size: 12px; font-weight: 600; letter-spacing: 0.5px; }
  .address { font-size: 9.5px; }
  .contact-list { list-style: none; display: flex; flex-direction: column; justify-content: center; gap: 3px; }
  .contact-item { display: flex; align-items: center; gap: 7px; }
  .contact-icon { width: 11px; height: 11px; flex: none; }
</style>
</head>
<body>

<section class="card card-back" aria-label="Back of business card">
  <div class="brand-lockup">
    <span class="brand-dot"></span>
    <div class="brand-name">BrookMint</div>
  </div>
  <div class="tagline">Rest easy through every visit</div>
</section>

<section class="card card-front" aria-label="Front of business card">
  <div class="front-header">
    <div class="brand-lockup">
      <span class="brand-dot"></span>
      <div class="brand-name">BrookMint</div>
    </div>
    <div class="tagline">Rest easy through every visit</div>
  </div>
  <div class="gold-rule"></div>
  <div class="front-footer">
    <div class="practitioner">
      <div class="practitioner-name">Rafael Okonkwo, DMD, MPH, MBA</div>
      <div class="address">
        418 North Pine Hollow Road<br>
        Suite 207915<br>
        Phoenix, Arizona 85093
      </div>
    </div>
    <ul class="contact-list">
      <li class="contact-item">
        <svg class="contact-icon" viewBox="0 0 24 24" fill="#fff"><path d="M6.6 10.8a15 15 0 0 0 6.6 6.6l2.2-2.2a1 1 0 0 1 1-.25 11.4 11.4 0 0 0 3.6.57 1 1 0 0 1 1 1V20a1 1 0 0 1-1 1A17 17 0 0 1 3 4a1 1 0 0 1 1-1h3.5a1 1 0 0 1 1 1 11.4 11.4 0 0 0 .57 3.6 1 1 0 0 1-.25 1z"/></svg>
        (877) 555-TOOL (8665)
      </li>
      <li class="contact-item">
        <svg class="contact-icon" viewBox="0 0 24 24" fill="#fff"><path d="M6.6 10.8a15 15 0 0 0 6.6 6.6l2.2-2.2a1 1 0 0 1 1-.25 11.4 11.4 0 0 0 3.6.57 1 1 0 0 1 1 1V20a1 1 0 0 1-1 1A17 17 0 0 1 3 4a1 1 0 0 1 1-1h3.5a1 1 0 0 1 1 1 11.4 11.4 0 0 0 .57 3.6 1 1 0 0 1-.25 1z"/></svg>
        (480) 555-TOOL (8665)
      </li>
      <li class="contact-item">
        <svg class="contact-icon" viewBox="0 0 24 24" fill="none" stroke="#fff" stroke-width="2"><rect x="3" y="5" width="18" height="14" rx="1"/><path d="M3 6l9 7 9-7"/></svg>
        Dr.Okonkwo@BrookMintDental.example
      </li>
      <li class="contact-item">
        <svg class="contact-icon" viewBox="0 0 24 24" fill="none" stroke="#fff" stroke-width="2"><circle cx="12" cy="12" r="9"/><path d="M3 12h18M12 3a14 14 0 0 1 0 18M12 3a14 14 0 0 0 0 18"/></svg>
        www.BrookMintDental.example
      </li>
    </ul>
  </div>
</section>

</body>
</html>
```